Lumo Nutrition Boost

We need a label designed for 4 different Vitamins. Dr. Lumo is a Chiropractor and would like to add few vitamins that help his patients and other people in need. Our logo is black and white which I will share below. We want something that stands out, attracts all age clients, and is easy to read and remember. Needs to be catchy just like the Brand Name - "Lumo" The Logo will be switched. Instead of it saying Chiropractic & Physical Therapy, it should say Nutrition on top and Boost on the bottom. Below is also my idea roughly on the designs, but open to your ideas and the name is what we want to go with. Also providing couple designs that were worked on under a different account by one of our collaborators. Thank You, Tova

```html
<!DOCTYPE html>
<html lang="en">
<head>
<meta charset="utf-8">
<title>Lumo – Supplement Labels</title>
<link rel="stylesheet" href="https://fonts.googleapis.com/css2?family=Bitter:wght@800&family=Montserrat:wght@600;700&display=swap">
<style>
  :root {
    --canvas: #ececec;
    --label: #ffffff;
    --ink: #2b2b2b;
    --band-dark: #2f2f2f;
    --green: #2fc455;
    --orange: #ffb530;
    --purple: #bd5cd1;
    --grey: #8e8e8e;
    --muted-ink: #3a3a3a;
  }
  * { box-sizing: border-box; margin: 0; padding: 0; }
  html, body { width: 1200px; height: 1200px; overflow: hidden; background: var(--canvas); }
  .canvas {
    width: 1200px; height: 1200px;
    display: flex; align-items: flex-end; justify-content: center;
    gap: 14px; padding-bottom: 100px;
  }
  .label {
    --accent: var(--ink);
    background: var(--label);
    width: 250px; height: 380px;
    position: relative;
    display: flex; flex-direction: column; align-items: center;
    border-top: 14px solid var(--accent);
    border-bottom: 14px solid var(--accent);
    box-shadow: 0 2px 10px rgba(0,0,0,.06);
  }
  .label--mend { --accent: var(--green); }
  .label--guard { --accent: var(--orange); width: 370px; height: 470px; border-width: 18px; }
  .label--ease { --accent: var(--purple); width: 262px; }
  .label--frame { --accent: var(--grey); }

  .brand {
    margin-top: 40px;
    display: flex; align-items: center; gap: 10px;
  }
  .brand__dot { width: 20px; height: 20px; border-radius: 50%; background: var(--ink); }
  .brand__name {
    font-family: "Montserrat", sans-serif; font-weight: 700;
    font-size: 38px; color: var(--ink); letter-spacing: 1px;
  }
  .label--guard .brand { margin-top: 50px; }
  .label--guard .brand__name { font-size: 50px; }
  .label--guard .brand__dot { width: 26px; height: 26px; }

  .product-name {
    margin-top: 60px;
    font-family: "Montserrat", sans-serif; font-weight: 700;
    font-size: 30px; letter-spacing: 1px;
    color: var(--accent);
    white-space: nowrap;
  }
  .label--guard .product-name { margin-top: 80px; font-size: 40px; }

  .ingredient {
    margin-top: 12px;
    background: var(--band-dark);
    width: 84%; height: 30px;
    display: flex; align-items: center; justify-content: center;
    font-family: "Bitter", serif; font-weight: 800;
    font-size: 15px; letter-spacing: 2px;
    color: var(--accent);
  }
  .label--guard .ingredient { height: 38px; font-size: 19px; }

  .icon-slot {
    position: absolute; right: 16px; bottom: 62px;
    width: 36px; height: 36px; border-radius: 50%;
    border: 2px solid var(--accent); opacity: .8;
  }
  .label--guard .icon-slot { width: 50px; height: 50px; bottom: 70px; }

  .count {
    margin-top: auto; margin-bottom: 14px;
    text-align: center; color: var(--muted-ink);
    font-family: "Montserrat", sans-serif;
  }
  .count__qty { font-weight: 700; font-size: 16px; }
  .count__type { font-weight: 600; font-size: 7.5px; letter-spacing: 1.5px; }
  .label--guard .count__qty { font-size: 20px; }
  .label--guard .count__type { font-size: 9px; }
</style>
</head>
<body>
<main class="canvas">

  <section class="label label--mend">
    <div class="brand"><span class="brand__dot"></span><span class="brand__name">Lumo</span></div>
    <h2 class="product-name">MEND PLUS</h2>
    <div class="ingredient">TURMERIC</div>
    <div class="icon-slot" role="img" aria-label="Recovery cross icon"></div>
    <div class="count"><div class="count__qty">60 CAPSULES</div><div class="count__type">DIETARY SUPPLEMENT</div></div>
  </section>

  <section class="label label--guard">
    <div class="brand"><span class="brand__dot"></span><span class="brand__name">Lumo</span></div>
    <h2 class="product-name">GUARD PLUS</h2>
    <div class="ingredient">MULTIVITAMIN</div>
    <div class="icon-slot" role="img" aria-label="Citrus slice icon"></div>
    <div class="count"><div class="count__qty">60 CAPSULES</div><div class="count__type">DIETARY SUPPLEMENT</div></div>
  </section>

  <section class="label label--ease">
    <div class="brand"><span class="brand__dot"></span><span class="brand__name">Lumo</span></div>
    <h2 class="product-name">EASE PLUS</h2>
    <div class="ingredient">OMEGA 3</div>
    <div class="icon-slot" role="img" aria-label="Omega 3 drop icon"></div>
    <div class="count"><div class="count__qty">60 CAPSULES</div><div class="count__type">DIETARY SUPPLEMENT</div></div>
  </section>

  <section class="label label--frame">
    <div class="brand"><span class="brand__dot"></span><span class="brand__name">Lumo</span></div>
    <h2 class="product-name">FRAME PLUS</h2>
    <div class="ingredient">VITAMIN D</div>
    <div class="icon-slot" role="img" aria-label="Bone icon"></div>
    <div class="count"><div class="count__qty">60 CAPSULES</div><div class="count__type">DIETARY SUPPLEMENT</div></div>
  </section>

</main>
</body>
</html>
```